依頼詳細
レスポンシブウェブデザインを意識したデザインでお願いします。

デザインに関しては、添付してあるデザインレイアウトシートを基にお願いします。
参考サイトのURLはデザインレイアウトシートに記載してあります。
色合いはグリーンかブルーを基調にお願いします。
新規のウェブサイトですので、既存サイトはありません。
ロゴも不要です。(後ではめ込むので社名だけテキストでレイアウトをお願いします。)
また、写真データも添付するので、レイアウトシートのイメージ画像に当て込んでください。

まずはパソコンサイトのデザインをお願いします。
当選後、スマホデザインをお願いします。

既存のテンプレートを使う場合は
テンプレート名を下記のような記載を提案の中にいれてください。
例:WordpressテーマはCorpLumen、デザインスキンは無料のQRN2019 LX4(http://corplumen.example/ex_plugin/qrnfuji2019_lx4/)をベースにデザインいたしました。
など

写真データで足りない場合は、一旦他のサイトや参考URLの写真をサンプルとして入れてください。(サンプルなどの表記をお願いします)
また、購入が必要な写真などを利用した場合は、Pixora Stock(https://stock.pixora-img.example/jp/)からファイル番号と価格を教えてください。
ページ数
1ページ
希望イメージ
シンプル 複雑
単色 カラフル
暗い 明るい
日常 高級
遊び心 厳粛
未来的 伝統的
女性的 男性的
希望する色
青系、緑系
納品ファイル
• イラストレーター形式 (.ai)
• フォトショップ形式 (.psd)
• PNG形式 (.png)
補足説明
上記のいずれか1つ。アウトラインありとなしの2つ。

こちらの要望を汲んで、デザインしていただきました。
ありがとうございました。

たくさんのご提案ありがとうございました。
次回もぜひ、よろしくお願い致します。

```html
<!DOCTYPE html>
<html lang="ja">
<head>
<meta charset="utf-8">
<title>有限会社蒼峰</title>
<link href="https://fonts.googleapis.com/css2?family=Noto+Sans+JP:wght@400;500;700&family=Noto+Serif+JP:wght@500;700;900&display=swap" rel="stylesheet">
<style>
:root{
  --blue:#1c67c9;
  --blue-deep:#13509f;
  --blue-soft:#a8c4ea;
  --blue-pale:#e7eef8;
  --teal-photo:#8fb0ab;
  --teal-dark:#5f837f;
  --ink:#222;
  --grey:#f2f2f2;
  --grey-mid:#9a9a9a;
  --white:#fff;
  --accent:#f1d000;
}
*{margin:0;padding:0;box-sizing:border-box}
html,body{width:1200px;height:4488px;overflow:hidden}
body{font-family:"Noto Sans JP",sans-serif;color:var(--ink);background:var(--white);position:relative}
.serif{font-family:"Noto Serif JP",serif}
section,header,footer{position:absolute;left:0;width:1200px}
.photo{position:absolute}

/* header + hero */
.hero{top:0;height:700px;overflow:hidden}
.hero .photo{inset:0;background:linear-gradient(160deg,#b5ccc8 0%,var(--teal-photo) 45%,#7d9f9a 100%)}
.hero .veil{position:absolute;inset:0;background:linear-gradient(180deg,rgba(255,255,255,.35),rgba(255,255,255,0) 30%)}
.site-header{top:0;height:72px;display:flex;align-items:center;justify-content:space-between;padding:0 40px}
.brand{display:flex;align-items:center;gap:12px;font-family:"Noto Serif JP",serif;font-weight:700;font-size:22px;color:var(--white);letter-spacing:.12em}
.brand .dot{width:34px;height:34px;border-radius:50%;border:2px solid var(--white)}
.global-nav{display:flex;gap:30px;font-size:14px;font-weight:500;color:var(--white)}
.hero-copy{position:absolute;left:590px;top:130px;color:var(--white);font-family:"Noto Serif JP",serif;font-weight:900;font-size:60px;line-height:1.45;letter-spacing:.08em;text-shadow:0 2px 10px rgba(0,0,0,.25)}
.hero-copy .line2{padding-left:10px}
.scroll-cue{position:absolute;left:584px;top:540px}
.hero-cut{position:absolute;left:0;bottom:0}

/* headings */
.sec-title{font-family:"Noto Serif JP",serif;font-weight:700;font-size:30px;letter-spacing:.1em;padding-left:16px;border-left:6px solid var(--blue);line-height:1.2}
.sec-sub{font-family:"Noto Serif JP",serif;font-size:15px;color:var(--blue);font-style:normal;margin-top:4px;padding-left:22px;letter-spacing:.05em}
.body-text{font-size:14px;line-height:2;letter-spacing:.06em}

/* features */
.features{top:720px;height:620px}
.features .panel{position:absolute;left:0;top:40px;width:560px;height:500px;background:linear-gradient(135deg,var(--blue-soft),#d4e2f4 70%,var(--blue-pale));clip-path:polygon(0 0,100% 0,88% 100%,0 100%)}
.features .panel-inner{position:absolute;left:80px;top:90px;width:380px}
.features .body-text{margin-top:34px}
.features .photo{left:560px;top:70px;width:640px;height:440px;background:linear-gradient(150deg,#cfd8dc,#9aa7ad 55%,#6f7d84)}

/* services */
.services{top:1360px;height:1000px}
.services .lines{position:absolute;inset:0}
.services .head{position:absolute;left:80px;top:20px;width:1040px}
.services .body-text{margin-top:24px}
.service-grid{position:absolute;left:80px;top:250px;width:1040px;display:grid;grid-template-columns:repeat(3,320px);column-gap:40px;row-gap:50px}
.card .photo{position:relative;width:320px;height:190px;background:linear-gradient(145deg,#c9d2d6,#8c989e)}
.card .photo.warm{background:linear-gradient(145deg,#b8a894,#6f6456)}
.card .photo.dark{background:linear-gradient(145deg,#7b8388,#3f464a)}
.card h3{text-align:center;font-family:"Noto Serif JP",serif;font-weight:500;font-size:16px;margin:14px 0 8px;letter-spacing:.3em}
.card p{font-size:12px;line-height:1.8;letter-spacing:.04em}
.card .more{position:absolute;left:50%;top:50%;transform:translate(-50%,-50%);background:var(--blue-deep);color:var(--white);font-size:13px;padding:8px 24px;letter-spacing:.1em;white-space:nowrap}

/* recruitment */
.recruit{top:2360px;height:700px}
.recruit .band{position:absolute;inset:0;background:linear-gradient(180deg,#eef3f9,#dfe8f3)}
.recruit .head{position:absolute;left:80px;top:60px}
.recruit .cols{position:absolute;left:80px;top:170px;width:1040px;display:grid;grid-template-columns:1fr 1fr;column-gap:60px}
.recruit .banner{position:absolute;left:64px;top:340px;width:1136px;height:320px;overflow:hidden}
.recruit .banner .photo{inset:0;background:linear-gradient(100deg,#c6cdd2 0%,#8e99a1 45%,#5c6a74 100%)}
.recruit .banner-copy{position:absolute;left:0;right:0;top:70px;text-align:center;color:var(--white);font-family:"Noto Serif JP",serif;font-weight:900;font-size:42px;line-height:1.5;letter-spacing:.08em;text-shadow:0 2px 8px rgba(0,0,0,.35)}
.recruit .banner-copy em{font-style:normal;color:var(--accent)}
.btn{display:inline-flex;align-items:center;justify-content:center;gap:16px;font-size:14px;letter-spacing:.1em}
.recruit .btn{position:absolute;left:468px;top:232px;width:200px;height:44px;background:var(--blue);color:var(--white)}

/* news */
.news{top:3100px;height:540px}
.news .box{position:absolute;left:64px;top:0;width:1072px;height:520px;background:var(--grey)}
.news .head{position:absolute;left:40px;top:40px}
.news-list{position:absolute;left:40px;top:150px;width:992px;list-style:none}
.news-list li{display:flex;align-items:center;height:64px;border-bottom:1px solid #d8d8d8;font-size:14px}
.news-list time{width:110px;color:#444}
.news-list .tag{width:70px;height:22px;background:var(--blue);color:var(--white);font-size:11px;display:flex;align-items:center;justify-content:center;margin-right:30px}
.news-list .title{flex:1}
.news .btn{position:absolute;left:446px;top:428px;width:180px;height:44px;background:#333;color:var(--white);font-size:13px}

/* contact */
.contact{top:3660px;height:450px;overflow:hidden}
.contact .photo{inset:0;background:linear-gradient(180deg,#9aa1a5,#6e767b)}
.contact .inner{position:absolute;left:0;right:0;top:60px;text-align:center;color:var(--white)}
.contact .lead{font-size:15px;letter-spacing:.1em;font-weight:500}
.contact .btn{margin-top:26px;width:400px;height:72px;background:var(--white);color:var(--blue);font-size:20px;font-weight:700}
.contact .tel{margin-top:30px;display:flex;align-items:center;justify-content:center;gap:14px;font-size:46px;font-weight:700;letter-spacing:.03em}
.contact .hours{font-size:14px;margin-top:4px;letter-spacing:.08em}

/* footer */
.footer-nav{top:4110px;height:70px;display:flex;justify-content:center;align-items:center;gap:34px;font-size:13px;background:var(--white)}
.site-footer{top:4180px;height:308px;background:var(--blue);color:var(--white)}
.site-footer .brand-block{position:absolute;left:340px;top:60px;display:flex;align-items:center;gap:18px}
.site-footer .mark{width:64px;height:64px;border-radius:50%;border:3px solid var(--white)}
.site-footer .name{font-family:"Noto Sans JP",sans-serif;font-weight:700;font-size:36px;letter-spacing:.12em}
.site-footer .roman{font-family:"Noto Sans JP",sans-serif;font-weight:700;font-size:20px;letter-spacing:.3em;margin-top:4px}
.site-footer address{position:absolute;left:760px;top:70px;font-style:normal;font-size:13px;line-height:1.9}
.site-footer .copy{position:absolute;left:0;right:0;bottom:26px;text-align:center;font-size:11px;opacity:.9}
</style>
</head>
<body>

<section class="hero">
  <div class="photo" role="img" aria-label="建設現場の足場資材が積まれた資材置き場の写真"></div>
  <div class="veil"></div>
  <header class="site-header">
    <div class="brand"><span class="dot"></span>有限会社蒼峰</div>
    <nav class="global-nav"><span>ホーム</span><span>お知らせ</span><span>会社案内</span><span>業務内容</span><span>採用情報</span><span>お問い合わせ</span></nav>
  </header>
  <h1 class="hero-copy"><span>建設現場の</span><br><span class="line2">『命』…ここにあり</span></h1>
  <svg class="scroll-cue" width="32" height="40" viewBox="0 0 32 40"><polyline points="4,8 16,20 28,8" fill="none" stroke="#fff" stroke-width="3"/><polyline points="4,22 16,34 28,22" fill="none" stroke="#fff" stroke-width="3"/></svg>
  <svg class="hero-cut" width="1200" height="80" viewBox="0 0 1200 80"><polygon points="0,80 1200,10 1200,80" fill="#fff"/></svg>
</section>

<section class="features">
  <div class="panel"></div>
  <div class="panel-inner">
    <h2 class="sec-title">当社の特徴</h2>
    <p class="sec-sub">-Features-</p>
    <p class="body-text">足場資材のレンタルと整備を通じて、安全な現場づくりを支えています。整備済みの資材を必要な時に必要な量だけお届けします。地域の建設現場と共に歩み続けてきた経験を活かし、確かな品質をお約束します。</p>
  </div>
  <div class="photo" role="img" aria-label="倉庫の前に整然と並ぶ足場資材の写真"></div>
</section>

<section class="services">
  <svg class="lines" width="1200" height="1000" viewBox="0 0 1200 1000"><g stroke="#dbe6f3" stroke-width="6" fill="none"><line x1="-50" y1="420" x2="1250" y2="120"/><line x1="200" y1="1000" x2="900" y2="180"/><line x1="600" y1="1000" x2="1250" y2="500"/></g></svg>
  <div class="head">
    <h2 class="sec-title">業務内容</h2>
    <p class="sec-sub">-Our Services-</p>
    <p class="body-text">仮設足場資材のレンタル、販売、整備、運搬までを一貫して行っています。現場の規模や工期に合わせて最適な資材をご提案し、整備工場で点検を済ませた安全な資材を迅速にお届けします。お気軽にご相談ください。</p>
  </div>
  <div class="service-grid">
    <article class="card"><div class="photo" role="img" aria-label="積み上げられた足場資材の写真"></div><h3>タイトル</h3><p>足場資材のレンタルを行っています。必要な分だけ短期間からご利用いただけます。</p></article>
    <article class="card"><div class="photo dark" role="img" aria-label="並べられた鋼製足場板の写真"><span class="more">タイトルの詳細へ</span></div><h3>タイトル</h3><p>鋼製足場板などの販売も承ります。用途に合わせた資材をご案内いたします。</p></article>
    <article class="card"><div class="photo" role="img" aria-label="倉庫に保管された資材の写真"></div><h3>タイトル</h3><p>自社倉庫で資材を保管し、ご注文に合わせて速やかに出荷いたします。</p></article>
    <article class="card"><div class="photo warm" role="img" aria-label="作業員が資材を整備している写真"></div><h3>タイトル</h3><p>返却された資材は一つずつ点検し、整備を行ってから再出荷しています。</p></article>
    <article class="card"><div class="photo" role="img" aria-label="かごに入れられた金具類の写真"></div><h3>タイトル</h3><p>クランプなどの金具類も豊富に揃え、細かなご要望にもお応えします。</p></article>
    <article class="card"><div class="photo dark" role="img" aria-label="工場内の整備設備の写真"></div><h3>タイトル</h3><p>専用設備を備えた整備工場で、資材の品質を保つ作業を行っています。</p></article>
  </div>
</section>

<section class="recruit">
  <div class="band"></div>
  <div class="head">
    <h2 class="sec-title">採用情報</h2>
    <p class="sec-sub">-Recruitment-</p>
  </div>
  <div class="cols">
    <p class="body-text">私たちと一緒に地域の建設現場を支える仲間を募集しています。未経験の方も先輩社員が丁寧に指導しますので安心してご応募ください。</p>
    <p class="body-text">資格取得の支援制度も整っています。長く働ける職場づくりを大切にし、一人ひとりの成長を応援しています。</p>
  </div>
  <div class="banner">
    <div class="photo" role="img" aria-label="工場で資材を扱う作業員の写真"></div>
    <p class="banner-copy">現場を支える「<em>プロ</em>」として、<br>一緒に働きませんか？</p>
    <a class="btn">採用情報はこちら</a>
  </div>
</section>

<section class="news">
  <div class="box">
    <div class="head">
      <h2 class="sec-title">お知らせ</h2>
      <p class="sec-sub">-News-</p>
    </div>
    <ul class="news-list">
      <li><time>2020.01.01</time><span class="tag">ニュース</span><span class="title">ホームページを公開しました。今後ともよろしくお願いいたします。</span><svg width="10" height="16" viewBox="0 0 10 16"><polyline points="2,2 8,8 2,14" fill="none" stroke="#333" stroke-width="2"/></svg></li>
      <li><time>2020.01.01</time><span class="tag">ニュース</span><span class="title">年末年始の営業日についてのお知らせです。ご確認ください。</span><svg width="10" height="16" viewBox="0 0 10 16"><polyline points="2,2 8,8 2,14" fill="none" stroke="#333" stroke-width="2"/></svg></li>
      <li><time>2020.01.01</time><span class="tag">ニュース</span><span class="title">採用情報を更新しました。詳しくは採用ページをご覧ください。</span><svg width="10" height="16" viewBox="0 0 10 16"><polyline points="2,2 8,8 2,14" fill="none" stroke="#333" stroke-width="2"/></svg></li>
      <li><time>2020.01.01</time><span class="tag">ニュース</span><span class="title">新しい整備設備を導入しました。より早くお届けいたします。</span><svg width="10" height="16" viewBox="0 0 10 16"><polyline points="2,2 8,8 2,14" fill="none" stroke="#333" stroke-width="2"/></svg></li>
    </ul>
    <a class="btn">過去のお知らせ<svg width="8" height="12" viewBox="0 0 8 12"><polyline points="1,1 6,6 1,11" fill="none" stroke="#fff" stroke-width="2"/></svg></a>
  </div>
</section>

<section class="contact">
  <div class="photo" role="img" aria-label="資材置き場に並ぶ足場資材の写真"></div>
  <div class="inner">
    <p class="lead">ご質問などお気軽にお問い合わせください</p>
    <a class="btn"><svg width="30" height="22" viewBox="0 0 30 22"><rect x="1" y="1" width="28" height="20" fill="none" stroke="#1c67c9" stroke-width="2.5"/><polyline points="1,1 15,12 29,1" fill="none" stroke="#1c67c9" stroke-width="2.5"/></svg>お問い合わせはこちら</a>
    <p class="tel"><svg width="40" height="40" viewBox="0 0 24 24"><path fill="#fff" d="M6.6 10.8c1.4 2.8 3.8 5.1 6.6 6.6l2.2-2.2c.3-.3.7-.4 1-.2 1.1.4 2.3.6 3.6.6.6 0 1 .4 1 1V20c0 .6-.4 1-1 1C10.6 21 3 13.4 3 4c0-.6.4-1 1-1h3.5c.6 0 1 .4 1 1 0 1.3.2 2.5.6 3.6.1.3 0 .7-.2 1z"/></svg>025-000-4170</p>
    <p class="hours">営業時間 8:00 ～ 17:30</p>
  </div>
</section>

<nav class="footer-nav"><span>ホーム</span><span>お知らせ</span><span>会社案内</span><span>業務内容</span><span>採用情報</span><span>お問い合わせ</span><span>個人情報保護方針</span><span>サイトマップ</span></nav>

<footer class="site-footer">
  <div class="brand-block">
    <span class="mark"></span>
    <div><p class="name">有限会社蒼峰</p><p class="roman">SOHO</p></div>
  </div>
  <address>〒940-0000<br>新潟県青葉市中央町1丁目2番3号<br>Tel：025-000-4170<br>Fax：025-000-4171</address>
  <p class="copy">Copyright © 2020 SOHO Co.,Ltd. All Rights Reserved.</p>
</footer>

</body>
</html>
```